Business Card Design - Property Management & Real Estate Services

I need a business card design for my company that I can print Pell Prints. The company is called Tarrow Management Company. It is a property management and real estate company. The design has to be clean and modern. I need two versions. One for my employee and one for me. However, the design will be the same, just different text. You can get a feel for the company by looking at our website at www.tarrowmanagement.example.

Industry/Entity Type

Property Management

Contact Information for Business Card

I will be using Pell.com to print my cards. I will most likely use the rounded edges card. I need two versions, however, they will be the same design. I need one for me and my employee.

Colors
3276b5
33a6d7

Requirements
Must have
• Company Logo
• Name of person
• Property Management & Real Estate Service
• Phone
• Email
• Website
• Address
• A space to place a QR code

```html
<!DOCTYPE html>
<html lang="en">
<head>
<meta charset="utf-8">
<title>Tarrow Management – Business Card</title>
<link rel="stylesheet" href="https://fonts.googleapis.com/css2?family=Lato:wght@400;700&display=swap">
<style>
  :root {
    --backdrop: #d9d9d9;
    --card-white: #ffffff;
    --brand-navy: #1a55a0;
    --brand-blue: #1848a0;
    --accent-blue: #6a9fd4;
    --accent-pale: #dbe7f5;
    --ink: #222222;
    --link-blue: #3276b5;
  }
  * { margin: 0; padding: 0; box-sizing: border-box; }
  html, body {
    width: 1200px; height: 802px; overflow: hidden;
    background: var(--backdrop);
    font-family: "Lato", Arial, sans-serif;
  }
  .canvas { position: relative; width: 1200px; height: 802px; }
  .card {
    position: absolute; top: 274px; width: 442px; height: 264px;
    overflow: hidden;
    box-shadow: 2px 3px 6px rgba(0,0,0,0.35);
  }
  .card-front { left: 136px; background: var(--card-white); }
  .card-back { left: 624px; background: var(--brand-navy); }
  .card-band {
    position: absolute; left: 0; bottom: 0; width: 100%; height: 7px;
    background: var(--accent-blue);
  }
  .decoration-area {
    position: absolute; left: 228px; top: 2px; width: 178px; height: 255px;
    background: linear-gradient(180deg, var(--card-white) 0%, var(--accent-pale) 100%);
  }
  .person { position: absolute; left: 24px; top: 112px; }
  .person-name {
    font-weight: 700; font-size: 15.5px; color: var(--brand-blue);
    line-height: 1.1;
  }
  .person-title { font-size: 11px; color: var(--ink); margin-top: 2px; }
  .address {
    position: absolute; left: 24px; top: 156px;
    font-size: 11px; line-height: 16px; color: var(--ink);
  }
  .contacts {
    position: absolute; left: 23px; top: 203px; list-style: none;
    font-size: 11px; color: var(--ink);
  }
  .contacts li { display: flex; align-items: center; height: 17px; white-space: nowrap; }
  .contacts svg { width: 13px; height: 13px; margin-right: 5px; flex: none; }
  .contacts .web { color: var(--link-blue); }
  .brand-name {
    position: absolute; left: 0; width: 100%; top: 152px;
    text-align: center; color: #ffffff;
    font-weight: 400; font-size: 40px; letter-spacing: 2px; line-height: 1;
  }
  .brand-sub {
    position: absolute; left: 0; width: 100%; top: 206px;
    text-align: center; color: var(--accent-blue);
    font-weight: 400; font-size: 10px; letter-spacing: 9px; padding-left: 9px;
  }
</style>
</head>
<body>
<main class="canvas">
  <section class="card card-front" aria-label="Card front">
    <div class="decoration-area" role="img" aria-label="Large brand mark decoration area"></div>
    <div class="person">
      <p class="person-name">DANIEL HARTWELL</p>
      <p class="person-title">Managing Director</p>
    </div>
    <p class="address">421, Address line here<br>Country Name, 45452</p>
    <ul class="contacts">
      <li>
        <svg viewBox="0 0 14 14" aria-hidden="true"><rect x="0.7" y="0.7" width="12.6" height="12.6" rx="2" fill="none" stroke="#1848a0" stroke-width="1.2"/><path d="M4.3 3.3l1.4-.3.8 2-1 .7c.5 1.2 1.3 2 2.5 2.5l.7-1 2 .8-.3 1.4c-3.4.3-6.4-2.7-6.1-6.1z" fill="#1848a0"/></svg>
        044-555 010 234
      </li>
      <li>
        <svg viewBox="0 0 14 14" aria-hidden="true"><rect x="0.5" y="2.5" width="13" height="9" fill="#1848a0"/><path d="M0.8 3l6.2 5 6.2-5" fill="none" stroke="#fff" stroke-width="1.1"/></svg>
        info@tarrowmail.example
      </li>
      <li class="web">
        <svg viewBox="0 0 14 14" aria-hidden="true"><g fill="none" stroke="#1848a0" stroke-width="1.1"><circle cx="7" cy="7" r="6"/><ellipse cx="7" cy="7" rx="2.6" ry="6"/><path d="M1 7h12M2 4h10M2 10h10"/></g></svg>
        www.tarrowmanagement.example
      </li>
    </ul>
    <div class="card-band"></div>
  </section>

  <section class="card card-back" aria-label="Card back">
    <p class="brand-name">TARROW</p>
    <p class="brand-sub">MANAGEMENT</p>
    <div class="card-band"></div>
  </section>
</main>
</body>
</html>
```